Consultants Need a Powerful New Image to Support a New Concept

We need a better image for an idea we have. Will be used in powerpoint but also in print (workbooks, handouts etc). The notion is that in any moment people in an organisation can choose to tell positive stories about what is going well, what they enjoy, what they are hopeful for or negative stories about what is wrong, not working or they are frustrated and pissed off about.

Target Market(s)

Leaders in organisations

Industry/Entity Type

It Support

Font styles to use
Sans Serif

Requirements
Must have
• The ability to build the image in powerpoint (at least add the text). Needs also to be used as a stand alone. Font and palette consistency with other materials. Some examples attached as well as font files and colour guidelines. Notice the left hand side of the model is about tell the stories and the right hand side is about how telling positive stories encourages others to seek more positive stories. On the right hand side down the bottom, the point is that these negative stories are so easy to join in on and they spread quickly and breed cynicism. Note the "Keelmark" running up and down the middle - keelmark model attached.
Nice to have
• A sense of momentum both up and down - the more positive stories we tell the more the organisation is energised and positive, the more negative stories (whingeing and complaining) the worse it is.

```html
<!DOCTYPE html>
<html lang="en">
<head>
<meta charset="utf-8">
<title>The Conversational Moment</title>
<link rel="stylesheet" href="https://fonts.googleapis.com/css2?family=Open+Sans:wght@400;600;700;800&display=swap">
<style>
  :root {
    --green: #a2c31b;
    --green-soft: #d2e390;
    --brown: #5e5141;
    --brown-soft: #b8b0a6;
    --overlap: #3d3a17;
    --ink: #2b2b2b;
    --brand: #2e3558;
    --white: #ffffff;
  }
  * { margin: 0; padding: 0; box-sizing: border-box; }
  html, body { width: 1200px; height: 690px; overflow: hidden; background: var(--white); }
  body { font-family: "Open Sans", Arial, sans-serif; color: var(--ink); }
  .canvas { position: relative; width: 1200px; height: 690px; }

  .bubbles { position: absolute; left: 0; top: 0; }

  .heading {
    position: absolute; width: 260px; text-align: center;
    font-weight: 700; font-size: 20px; line-height: 26px;
  }
  .heading--bright { left: 350px; top: 120px; color: var(--green); }
  .heading--dark { left: 578px; top: 120px; color: var(--brown); }

  .bubble-text {
    position: absolute; width: 180px; text-align: center;
    color: var(--white); font-weight: 700; font-size: 17px; line-height: 24px;
  }
  .bubble-text--seek { left: 354px; top: 317px; }
  .bubble-text--join { left: 636px; top: 317px; }

  .question {
    position: absolute; left: 570px; top: 322px; width: 60px; text-align: center;
    color: var(--white); font-weight: 800; font-size: 58px; line-height: 70px;
  }

  .effect {
    position: absolute; font-size: 16.5px; line-height: 21px;
    display: flex; align-items: center;
  }
  .effect--left { right: 924px; justify-content: flex-end; text-align: right; padding-right: 10px; border-right: 3px solid var(--green); }
  .effect--right { left: 920px; text-align: left; padding-left: 11px; border-left: 3px solid var(--brown); }
  .effect { height: 42px; }

  .stage {
    position: absolute; font-weight: 800; font-size: 24px; line-height: 28px; letter-spacing: 0.5px;
  }
  .stage--left { left: 282px; color: var(--green-soft); }
  .stage--right { right: 284px; text-align: right; color: var(--brown-soft); }

  .caption {
    position: absolute; left: 0; width: 1200px; top: 558px; text-align: center;
    font-weight: 700; font-size: 17.5px; letter-spacing: 0.4px;
  }

  .brand {
    position: absolute; left: 90px; top: 605px;
    display: flex; align-items: center; gap: 10px;
    color: var(--brand); font-size: 33px; font-weight: 400; line-height: 40px;
  }
  .brand__dot { width: 30px; height: 30px; border-radius: 50%; background: var(--brand); }
</style>
</head>
<body>
<main class="canvas">
  <svg class="bubbles" width="1200" height="690" viewBox="0 0 1200 690" aria-hidden="true">
    <defs>
      <clipPath id="bright-circle"><circle cx="498" cy="358" r="146"/></clipPath>
    </defs>
    <g class="bubble bubble--bright" fill="var(--green)">
      <circle cx="498" cy="358" r="146"/>
      <path d="M380,440 C378,462 366,474 348,479 C385,484 420,476 446,460 Z"/>
    </g>
    <g class="bubble bubble--dark" fill="var(--brown)">
      <circle cx="702" cy="358" r="146"/>
      <path d="M820,440 C822,462 834,474 852,479 C815,484 780,476 754,460 Z"/>
    </g>
    <circle class="bubble-overlap" cx="702" cy="358" r="146" fill="var(--overlap)" clip-path="url(#bright-circle)"/>
  </svg>

  <h2 class="heading heading--bright">TELL STORIES:<br>Bright Spots &amp;<br>Possibility</h2>
  <h2 class="heading heading--dark">TELL STORIES:<br>Complaint &amp;<br>Failure</h2>

  <p class="bubble-text bubble-text--seek">SEEK STORIES:<br>Catch People<br>Doing Things<br>Right</p>
  <p class="bubble-text bubble-text--join">JOIN STORIES:<br>Cynicism,<br>Sarcasm &amp;<br>Negativity</p>
  <p class="question">?</p>

  <ul class="effects effects--bright" style="list-style:none">
    <li class="effect effect--left" style="top:199px">Changes<br>Awareness</li>
    <li class="effect effect--left" style="top:269px">Gives Insight,<br>Shapes Beliefs</li>
    <li class="effect effect--left" style="top:341px">Builds<br>Confidence</li>
    <li class="effect effect--left" style="top:412px">Encourages<br>Proactive Behaviour</li>
    <li class="effect effect--left" style="top:483px">Supports<br>Performance</li>
  </ul>
  <ul class="effects effects--dark" style="list-style:none">
    <li class="effect effect--right" style="top:199px">Fuels Unhelpful<br>Beliefs</li>
    <li class="effect effect--right" style="top:269px">Builds Negative<br>energy</li>
    <li class="effect effect--right" style="top:341px">Destroys<br>Confidence</li>
    <li class="effect effect--right" style="top:412px">Discourages<br>Effort and Action</li>
    <li class="effect effect--right" style="top:483px">Undermines<br>Performance</li>
  </ul>

  <span class="stage stage--left" style="top:242px">SEE</span>
  <span class="stage stage--left" style="top:312px">BE</span>
  <span class="stage stage--left" style="top:383px">DO</span>
  <span class="stage stage--left" style="top:454px">GET</span>
  <span class="stage stage--right" style="top:242px">SEE</span>
  <span class="stage stage--right" style="top:312px">BE</span>
  <span class="stage stage--right" style="top:383px">DO</span>
  <span class="stage stage--right" style="top:454px">GET</span>

  <p class="caption">THE CONVERSATIONAL MOMENT</p>

  <div class="brand"><span class="brand__dot"></span><span class="brand__name">Kestrel</span></div>
</main>
</body>
</html>
```